Software engineering company needs business card

I need a cool business card. Company: Byte Merano Larchwood Ave 41 58213 Dunmere Name: Gerald Hofmann CEO / Managing Director & Owner

Industry/Entity Type

Business

```html
<!DOCTYPE html>
<html lang="de">
<head>
<meta charset="utf-8">
<title>Byte Merano – Visitenkarte</title>
<link rel="stylesheet" href="https://fonts.googleapis.com/css2?family=Source+Sans+3:wght@400;600&display=swap">
<style>
  :root {
    --stage: #3b342f;
    --card: #121212;
    --green: #7ed321;
    --white: #f2f2f2;
    --text: #d6d6d6;
    --rule: #5a5a5a;
  }
  * { margin: 0; padding: 0; box-sizing: border-box; }
  html, body { width: 1200px; height: 769px; overflow: hidden; }
  body {
    background: var(--stage);
    font-family: "Source Sans 3", "Helvetica Neue", Arial, sans-serif;
    position: relative;
  }
  .card {
    position: absolute;
    top: 229px;
    width: 540px;
    height: 310px;
    background: var(--card);
    border-radius: 3px;
    box-shadow: 0 10px 30px rgba(0,0,0,.45);
  }
  .card--front { left: 40px; }
  .card--back { left: 620px; }

  .brand {
    position: absolute;
    font-weight: 600;
    letter-spacing: 0.18em;
    text-transform: uppercase;
    white-space: nowrap;
  }
  .card--front .brand {
    color: var(--green);
    font-size: 30px;
    left: 210px;
    top: 70px;
  }
  .card--back .brand {
    color: var(--white);
    font-size: 40px;
    left: 0; right: 0;
    top: 128px;
    text-align: center;
  }

  .rule {
    position: absolute;
    height: 1px;
    background: var(--rule);
  }
  .rule--long { left: 160px; right: 24px; top: 160px; }
  .rule--short { left: 26px; width: 200px; top: 228px; }

  .person { position: absolute; left: 26px; top: 178px; }
  .person__name {
    color: var(--green);
    font-weight: 600;
    font-size: 20px;
    text-transform: uppercase;
    line-height: 1.1;
  }
  .person__title { color: var(--text); font-size: 15px; margin-top: 2px; }

  .address {
    position: absolute;
    right: 24px;
    top: 170px;
    text-align: right;
    color: var(--text);
    font-size: 15px;
    line-height: 1.3;
  }

  .contact {
    position: absolute;
    left: 26px;
    top: 238px;
    list-style: none;
    color: var(--text);
    font-size: 15px;
    line-height: 1.35;
  }
  .contact li { display: flex; align-items: center; gap: 10px; }
  .contact svg { width: 13px; height: 13px; fill: var(--green); flex: none; }
</style>
</head>
<body>
  <section class="card card--front" aria-label="Vorderseite">
    <div class="brand">Byte Merano</div>
    <div class="rule rule--long"></div>

    <div class="person">
      <div class="person__name">Gerald Hofmann</div>
      <div class="person__title">CEO / Geschäftsführer &amp; Inhaber</div>
    </div>
    <div class="rule rule--short"></div>

    <ul class="contact">
      <li>
        <svg viewBox="0 0 16 16" aria-hidden="true"><path d="M3.2 1.5l2.3 2.4-1.2 1.9c.9 2 2.6 3.7 4.6 4.6l1.9-1.2 2.4 2.3-1.3 2.5C6.6 13.8 2.2 9.4 .7 4.1z"/></svg>
        (555) 014-2290
      </li>
      <li>
        <svg viewBox="0 0 16 16" aria-hidden="true"><path d="M4 1h8v14H4zM5.5 2.5v9.5h5V2.5z"/></svg>
        (555) 017-3846
      </li>
      <li>
        <svg viewBox="0 0 16 16" aria-hidden="true"><path d="M1 3h14v10H1zM2.5 4.5 8 9l5.5-4.5z"/></svg>
        gerald@bytemerano.example
      </li>
    </ul>

    <address class="address" style="font-style:normal">
      Larchwood Ave 41<br>
      58213 Dunmere<br>
      www.bytemerano.example
    </address>
  </section>

  <section class="card card--back" aria-label="Rückseite">
    <div class="brand">Byte Merano</div>
  </section>
</body>
</html>
```